Horse related business entrepreneur needs a business card

I need a business card design for my horse related business. The enterprise is Copper Vale LLC and I have 3 businesses (headquartered at 2 locations): 1. property management where we rent horse stalls and apartments at a thoroughbred training center outside Ocala; 2. a medium sized transportation service in central Florida that sells horse bedding and removes used horse bedding from horse farms; and horse racing

```html
<!DOCTYPE html>
<html lang="en">
<head>
<meta charset="utf-8">
<title>Copper Vale LLC — Business Card</title>
<link href="https://fonts.googleapis.com/css2?family=Didact+Gothic&display=swap" rel="stylesheet">
<style>
  :root {
    --backdrop: #e9e9e9;
    --slate: #29333a;
    --paper: #ffffff;
    --accent: #f0872a;
    --ink-light: #e6eaec;
    --rule: #cfd5d8;
  }
  html, body {
    margin: 0;
    width: 1200px;
    height: 991px;
    overflow: hidden;
    background: var(--backdrop);
    font-family: "Didact Gothic", "Helvetica Neue", Arial, sans-serif;
  }
  .stage {
    position: relative;
    width: 1200px;
    height: 991px;
  }
  .card {
    position: absolute;
    top: 350px;
    width: 500px;
    height: 292px;
    border-radius: 14px;
    overflow: hidden;
  }
  .card--front {
    left: 80px;
    background: var(--slate);
    display: flex;
    align-items: center;
    justify-content: center;
  }
  .card--front .company-name {
    color: var(--ink-light);
    font-size: 32px;
    white-space: nowrap;
  }
  .card--back {
    left: 620px;
    background: var(--paper);
  }
  .card__panel {
    position: absolute;
    inset: 0;
  }
  .card--back .company-name {
    position: absolute;
    left: 20px;
    top: 38px;
    color: var(--slate);
    font-size: 23px;
    line-height: 1;
    white-space: nowrap;
  }
  .holder {
    position: absolute;
    right: 26px;
    top: 36px;
    color: var(--paper);
    white-space: nowrap;
  }
  .holder__name {
    font-size: 23px;
    line-height: 1;
  }
  .holder__role {
    font-size: 13px;
    margin-top: 2px;
  }
  .contact {
    position: absolute;
    left: 190px;
    right: 12px;
    top: 192px;
    border-top: 1px solid var(--rule);
    padding-top: 6px;
    color: var(--ink-light);
    font-size: 11px;
    line-height: 14px;
    white-space: nowrap;
  }
  .contact__row {
    display: flex;
    align-items: flex-start;
    gap: 5px;
  }
  .contact__icon {
    flex: 0 0 auto;
    width: 12px;
    height: 12px;
    margin-top: 1px;
  }
</style>
</head>
<body>
<main class="stage">

  <section class="card card--front" aria-label="Card front">
    <span class="company-name">Copper Vale LLC</span>
  </section>

  <section class="card card--back" aria-label="Card back">
    <svg class="card__panel" width="500" height="292" viewBox="0 0 500 292" aria-hidden="true">
      <path d="M242 0 H500 V292 H168 Z" fill="var(--slate)"/>
      <path d="M236 0 L162 292" stroke="var(--slate)" stroke-width="1.4" fill="none"/>
    </svg>

    <span class="company-name">Copper Vale LLC</span>

    <div class="holder">
      <div class="holder__name">Dana Whitfield</div>
      <div class="holder__role">Owner</div>
    </div>

    <div class="contact">
      <div class="contact__row">
        <svg class="contact__icon" viewBox="0 0 12 12" aria-hidden="true">
          <rect width="12" height="12" rx="1.5" fill="var(--accent)"/>
          <path d="M6 2.2a2.6 2.6 0 0 1 2.6 2.6C8.6 6.8 6 9.8 6 9.8S3.4 6.8 3.4 4.8A2.6 2.6 0 0 1 6 2.2z" fill="var(--slate)"/>
          <circle cx="6" cy="4.8" r="0.9" fill="var(--accent)"/>
        </svg>
        <div>1520 SE Meadow Run, Fairfield, FL 32600<br>7710 Linden Hollow Rd, Ashford, VA 22900</div>
      </div>
      <div class="contact__row">
        <svg class="contact__icon" viewBox="0 0 12 12" aria-hidden="true">
          <rect width="12" height="12" rx="1.5" fill="var(--accent)"/>
          <path d="M3.6 2.4l1.4 1.6-.8 1.1c.5 1.1 1.4 2 2.6 2.6l1.1-.8 1.6 1.4-.9 1.3C6.4 9.4 2.6 5.6 2.4 3.3z" fill="var(--slate)"/>
        </svg>
        <div>p: (555) 014-2287<br>f: (555) 016-7730</div>
      </div>
      <div class="contact__row">
        <svg class="contact__icon" viewBox="0 0 12 12" aria-hidden="true">
          <rect width="12" height="12" rx="1.5" fill="var(--accent)"/>
          <rect x="2.3" y="3.5" width="7.4" height="5" fill="var(--slate)"/>
          <path d="M2.3 3.5L6 6.4l3.7-2.9" stroke="var(--accent)" stroke-width="0.8" fill="none"/>
        </svg>
        <div>dana@coppervale.com</div>
      </div>
    </div>
  </section>

</main>
</body>
</html>
```